Play on Words (French Puns)

Cover (11 x 17.8 cm) for a book of French plays on words. (Author: "Mathis Lobry" Title: "The Tricksters" Subtitle "Verbal Treats To Nibble" Publisher (at the bottom of the page): "Quill Press"

Target Market(s)

General public

Industry/Entity Type

Book Publisher

Colors

Designer to choose colors to be used in the design.

Requirements
Must have
• "Unserious" look
Should not have
• Eiffel Tower, triumphal arch (it's a book on French language, not on France)

```html
<!DOCTYPE html>
<html lang="en">
<head>
<meta charset="utf-8">
<title>The Tricksters — Mathis Lobry</title>
<link rel="stylesheet" href="https://fonts.googleapis.com/css2?family=Bowlby+One&family=EB+Garamond:wght@600&family=Luckiest+Guy&family=Oswald:wght@400&display=swap">
<style>
  :root {
    --surround: #000000;
    --paper: #ffffff;
    --ink-grey: #5f5d5f;
    --publisher-grey: #4a4a4a;
    --gold: #ecbd3c;
    --orange: #ef8a3a;
    --teal: #52dfd6;
    --yellow: #efbf3e;
    --green: #45dc88;
    --blue: #29a9e3;
    --pink: #e25a88;
    --magenta: #ee6bdc;
    --shadow-tint: #fde8cc;
  }
  * { margin: 0; padding: 0; box-sizing: border-box; }
  html, body {
    width: 1026px;
    height: 1200px;
    overflow: hidden;
    background: var(--surround);
  }
  .stage {
    position: relative;
    width: 1026px;
    height: 1200px;
  }
  .cover {
    position: absolute;
    left: 249px;
    top: 150px;
    width: 561px;
    height: 901px;
    background: var(--paper);
  }
  .title {
    position: absolute;
    left: 25px;
    top: 190px;
    width: 505px;
    height: 262px;
    overflow: visible;
  }
  .title text {
    font-family: "Luckiest Guy", "Arial Black", sans-serif;
  }
  .title .echo { fill: var(--shadow-tint); }
  .c-orange { fill: var(--orange); }
  .c-teal { fill: var(--teal); }
  .c-yellow { fill: var(--yellow); }
  .c-green { fill: var(--green); }
  .c-blue { fill: var(--blue); }
  .c-pink { fill: var(--pink); }
  .c-magenta { fill: var(--magenta); }
  .subtitle {
    position: absolute;
    left: 0;
    right: 0;
    top: 466px;
    text-align: center;
    font-family: "Bowlby One", "Arial Black", sans-serif;
    font-size: 33px;
    line-height: 1;
    letter-spacing: 0.5px;
    color: var(--ink-grey);
    text-transform: uppercase;
    white-space: nowrap;
  }
  .author {
    position: absolute;
    left: 0;
    right: 0;
    top: 578px;
    text-align: center;
    font-family: "EB Garamond", Garamond, serif;
    font-weight: 600;
    font-size: 52px;
    line-height: 1;
    color: var(--gold);
    text-transform: uppercase;
  }
  .publisher {
    position: absolute;
    left: 0;
    right: 0;
    top: 809px;
    text-align: center;
    font-family: "Oswald", "Arial Narrow", sans-serif;
    font-size: 24px;
    line-height: 1;
    color: var(--publisher-grey);
    text-transform: uppercase;
  }
</style>
</head>
<body>
  <div class="stage">
    <article class="cover">
      <svg class="title" viewBox="0 0 505 262" aria-label="The Tricksters">
        <text class="echo" x="131" y="122" font-size="118" textLength="260" lengthAdjust="spacingAndGlyphs">THE</text>
        <text x="125" y="116" font-size="118" textLength="260" lengthAdjust="spacingAndGlyphs"><tspan class="c-orange">T</tspan><tspan class="c-teal">H</tspan><tspan class="c-pink">E</tspan></text>
        <text class="echo" x="9" y="254" font-size="110" textLength="495" lengthAdjust="spacingAndGlyphs">TRICKSTERS</text>
        <text x="3" y="248" font-size="110" textLength="495" lengthAdjust="spacingAndGlyphs"><tspan class="c-yellow">T</tspan><tspan class="c-magenta">R</tspan><tspan class="c-yellow">I</tspan><tspan class="c-green">C</tspan><tspan class="c-yellow">K</tspan><tspan class="c-blue">S</tspan><tspan class="c-yellow">T</tspan><tspan class="c-orange">E</tspan><tspan class="c-pink">R</tspan><tspan class="c-yellow">S</tspan></text>
      </svg>
      <p class="subtitle">Verbal Treats To Nibble</p>
      <p class="author">Mathis Lobry</p>
      <p class="publisher">Quill Press</p>
    </article>
  </div>
</body>
</html>
```